Upscale business cards needed for family business

We need professional business cards created for several family members. We are a family business holding company. We would like these relatively simple and straightforward, but also with a unique element to set them apart. Probably stick with neutral and simple colors - white, grey etc. We need space for the traditional elements, including name, title, address, email/phone number. And we will be creating several from this template so it needs to be template that is easy to switch information in and out of.

Industry/Entity Type

Business

Contact Information for Business Card

Please include the attached Dunmore Ventures logo.

Requirements
Must have
• The attached Dunmore Ventures logo.

```html
<!DOCTYPE html>
<html lang="en">
<head>
<meta charset="utf-8">
<title>Dunmore Ventures — Business Card</title>
<link rel="stylesheet" href="https://fonts.googleapis.com/css2?family=Alegreya+Sans+SC:wght@700&family=Cinzel:wght@400&family=Courier+Prime&family=Lato:wght@400;700;900&display=swap">
<style>
  :root {
    --page-bg: #e9e7e3;
    --card-white: #ffffff;
    --band-black: #030303;
    --edge-grey: #585858;
    --rule-grey: #9a9a9a;
    --ink: #111111;
    --ink-soft: #8a8a8a;
    --icon-grey: #7a7a7a;
  }
  * { box-sizing: border-box; margin: 0; padding: 0; }
  html, body {
    width: 1200px; height: 799px; overflow: hidden;
    background: var(--page-bg);
  }
  .card {
    position: absolute; left: 100px; top: 114px;
    width: 1000px; height: 571px;
    background: var(--card-white);
    box-shadow: 0 6px 22px rgba(0,0,0,0.18);
    overflow: hidden;
  }
  .brand-band {
    position: absolute; left: 40px; top: 0;
    width: 262px; height: 100%;
    background: var(--band-black);
    display: flex; align-items: center; justify-content: center;
  }
  .brand-name {
    font-family: "Cinzel", serif;
    font-size: 30px; line-height: 1.25;
    color: var(--card-white);
    text-align: center; letter-spacing: 0.04em;
  }
  .edge-band {
    position: absolute; right: 0; top: 0;
    width: 46px; height: 100%;
    background: var(--edge-grey);
  }
  .details {
    position: absolute; left: 345px; top: 52px; width: 560px;
  }
  .person-name {
    font-family: "Alegreya Sans SC", sans-serif;
    font-weight: 700; font-size: 50px; line-height: 1;
    color: var(--ink); letter-spacing: 0.03em;
  }
  .person-title {
    font-family: "Courier Prime", monospace;
    font-size: 24px; color: var(--ink-soft);
    margin-top: 6px; letter-spacing: 0.06em;
  }
  .rule {
    height: 3px; background: var(--rule-grey);
    margin: 18px 0 16px;
  }
  .company {
    font-family: "Lato", sans-serif;
    font-size: 34px; color: var(--ink); letter-spacing: 0.02em;
  }
  .company strong { font-weight: 900; }
  .company small { font-size: 16px; }
  .address {
    font-family: "Lato", sans-serif;
    font-size: 20px; color: var(--ink); margin-top: 6px;
  }
  .contact-list { list-style: none; margin-top: 6px; }
  .contact-item {
    display: flex; align-items: center; gap: 22px;
    font-family: "Lato", sans-serif; font-size: 22px; color: var(--ink);
    height: 50px;
  }
  .contact-icon { width: 24px; height: 24px; flex: none; }
</style>
</head>
<body>
  <section class="card" aria-label="Dunmore Ventures business card">
    <div class="brand-band">
      <p class="brand-name">Dunmore<br>Ventures</p>
    </div>

    <div class="details">
      <h1 class="person-name">Name Surname</h1>
      <p class="person-title">Designation</p>
      <div class="rule"></div>
      <p class="company"><strong>DUNMORE</strong> VENTURES <small>INC.</small></p>
      <p class="address">118B W. Alder Creek Rd. Marlow, TX. 75001</p>
      <div class="rule"></div>
      <ul class="contact-list">
        <li class="contact-item">
          <svg class="contact-icon" viewBox="0 0 24 24" aria-hidden="true">
            <circle cx="12" cy="12" r="11" fill="var(--icon-grey)"/>
            <path d="M8.5 6.5l2 2.2-1.2 1.6c.8 1.7 2 2.9 3.7 3.7l1.6-1.2 2.2 2-1.3 2c-4.4-.4-8.3-4.3-8.7-8.7z" fill="#fff"/>
          </svg>
          (555) 014 - 2290
        </li>
        <li class="contact-item">
          <svg class="contact-icon" viewBox="0 0 24 24" aria-hidden="true">
            <circle cx="12" cy="12" r="11" fill="var(--icon-grey)"/>
            <circle cx="12" cy="12" r="6" fill="none" stroke="#fff" stroke-width="1.4"/>
            <ellipse cx="12" cy="12" rx="2.6" ry="6" fill="none" stroke="#fff" stroke-width="1.2"/>
            <path d="M6 12h12" stroke="#fff" stroke-width="1.2"/>
          </svg>
          www.DunmoreVentures.co
        </li>
        <li class="contact-item">
          <svg class="contact-icon" viewBox="0 0 24 24" aria-hidden="true">
            <circle cx="12" cy="12" r="11" fill="var(--icon-grey)"/>
            <rect x="6" y="8" width="12" height="8.5" rx="1" fill="#fff"/>
            <path d="M6.5 8.6l5.5 4.2 5.5-4.2" fill="none" stroke="var(--icon-grey)" stroke-width="1.2"/>
          </svg>
          Reed@DunmoreVentures.co
        </li>
      </ul>
    </div>

    <div class="edge-band"></div>
  </section>
</body>
</html>
```